A Web3 (Blockchain) Company need a Web Design

Hi from NineHalfMark.
We need a web design for a Blockchain company focused on infrastructure. We are building infrastructure that make people with non-blockchain knowledge and experience can build blockchain platform/service easier.

Our logo will have bridge/road ambience.
We also think about some blue color.
But please propose your idea.

We want the website to represent us in "Reliable", "Secure", and "Make your blockchain related development easier".

I include sales deck to make you understand more about our business.
We expect the design to be in figma.

```html
<!DOCTYPE html>
<html lang="en">
<head>
<meta charset="utf-8">
<title>NineHalfMark — Web3 Infrastructure</title>
<link rel="stylesheet" href="https://fonts.googleapis.com/css2?family=Montserrat:wght@400;500;600;700;800&family=Poppins:wght@300;400;500;600&display=swap">
<style>
:root{
  --blue:#1a6ce8;
  --blue-soft:#3d8ef0;
  --ink:#1f1f1f;
  --text:#3a3a3a;
  --muted:#6a6a6a;
  --band:#f3f3f3;
  --card:#eeeeee;
  --white:#ffffff;
  --navy:#0e2e5c;
  --line:#d9d9d9;
}
*{box-sizing:border-box;margin:0;padding:0}
html,body{width:1200px;height:4890px;overflow:hidden;background:var(--white)}
body{font-family:"Poppins",sans-serif;color:var(--text)}
.page{position:relative;width:1200px;height:4890px;overflow:hidden}
.section{position:absolute;left:0;width:1200px}
.abs{position:absolute}
.heading{font-family:"Montserrat",sans-serif;font-weight:800;color:var(--ink);letter-spacing:.3px}
.rule{position:absolute;height:2px;background:var(--blue);width:58px}
.btn{position:absolute;background:var(--blue);color:var(--white);font-family:"Montserrat",sans-serif;font-weight:700;font-size:13px;display:flex;align-items:center;justify-content:center;letter-spacing:.3px}
.visual{position:absolute}

/* header */
.site-header{top:0;height:133px}
.brand{position:absolute;left:133px;top:44px;display:flex;align-items:center;gap:10px;font-family:"Montserrat",sans-serif;font-weight:700;font-size:24px;color:var(--blue)}
.brand-mark{width:14px;height:14px;background:var(--blue)}
.nav{position:absolute;right:132px;top:41px;display:flex;gap:8px;font-family:"Poppins",sans-serif;font-size:12.5px;color:var(--ink)}
.nav span{padding:4px 10px}
.nav .active{background:var(--blue);color:var(--white)}

/* hero */
.hero{top:133px;height:520px}
.hero-kicker{left:131px;top:22px;font-family:"Montserrat",sans-serif;font-weight:700;font-size:17px;color:var(--ink)}
.hero-title{left:129px;top:46px;font-family:"Montserrat",sans-serif;font-weight:800;font-size:42px;color:var(--blue);letter-spacing:1px}
.check-list{position:absolute;list-style:none}
.check-list li{position:relative;padding-left:38px}
.check-list svg{position:absolute;left:0;top:2px;width:20px;height:20px}
.hero-list{left:131px;top:130px;width:400px;font-size:13.5px;line-height:19px;color:var(--text)}
.hero-list li{margin-bottom:29px}
.hero-photo{left:560px;top:2px;width:508px;height:448px;background:linear-gradient(160deg,#eef1f4 0%,#d9dee4 55%,#b9c1ca 100%)}

/* nutshell */
.nutshell{top:653px;height:460px;background:var(--band)}
.diagram-art{left:210px;top:90px;width:300px;height:250px;border-radius:50%;background:radial-gradient(circle,#f3f3f3 30%,#e2e2e2 60%,#f3f3f3 72%)}
.diagram-label{position:absolute;font-family:"Montserrat",sans-serif;font-weight:700;font-size:11px;color:var(--ink);transform:translateX(-50%);white-space:nowrap}
.nutshell-title{left:636px;top:66px;font-size:22px}
.nutshell-copy{left:638px;top:150px;width:410px;font-size:15.5px;line-height:25.5px;color:var(--text)}

/* trust */
.trust{top:1113px;height:502px}
.trust-kicker{left:0;width:1200px;top:52px;text-align:center;font-size:15px;color:var(--ink)}
.trust-title{left:0;width:1200px;top:78px;text-align:center;font-size:22px}
.trust-sub{left:0;width:1200px;top:112px;text-align:center;font-family:"Montserrat",sans-serif;font-weight:700;font-size:15px;color:var(--ink)}
.trust-card{position:absolute;top:198px;width:177px;height:224px;background:var(--white);box-shadow:0 2px 10px rgba(0,0,0,.09);text-align:center}
.trust-card svg{position:absolute;left:63px;top:36px;width:52px;height:52px}
.trust-card p{position:absolute;left:10px;right:10px;top:118px;font-size:14px;line-height:19px;color:var(--ink)}

/* products */
.products{top:1615px;height:1073px}
.product-card{position:absolute;width:454px;height:483px;background:var(--card);text-align:center}
.product-brand{position:absolute;left:0;right:0;top:35px;font-size:16.5px;color:var(--ink);letter-spacing:.5px}
.product-title{position:absolute;left:0;right:0;top:62px;font-family:"Montserrat",sans-serif;font-weight:800;font-size:19.5px;color:var(--ink)}
.product-sub{position:absolute;left:0;right:0;top:92px;font-size:15.5px;line-height:21px;color:var(--ink)}
.product-art{position:absolute;left:80px;right:80px;top:135px;height:215px;border-radius:110px}
.feature-list{position:absolute;list-style:none;font-size:11.5px;line-height:15px;color:var(--text);text-align:left}
.feature-list li{position:absolute;padding-left:14px;width:185px}
.feature-list li::before{content:"";position:absolute;left:0;top:4px;border-left:5px solid var(--ink);border-top:3.5px solid transparent;border-bottom:3.5px solid transparent}

/* team */
.team{top:2688px;height:627px;background:var(--band)}
.team-title{left:0;width:1200px;top:55px;text-align:center;font-size:22px}
.team-sub{left:0;width:1200px;top:88px;text-align:center;font-family:"Montserrat",sans-serif;font-weight:700;font-size:15px;color:var(--ink)}
.member{position:absolute;top:162px;width:296px;height:408px;background:var(--white);box-shadow:0 2px 10px rgba(0,0,0,.07);text-align:center}
.member-photo{position:absolute;left:0;top:0;width:100%;height:253px}
.member-name{position:absolute;left:0;right:0;top:283px;font-family:"Montserrat",sans-serif;font-weight:700;font-size:14px;color:var(--ink)}
.member-role{position:absolute;left:0;right:0;top:309px;font-family:"Montserrat",sans-serif;font-weight:600;font-size:13.5px;color:var(--ink)}
.member-bio{position:absolute;left:14px;right:14px;top:345px;font-size:12.5px;line-height:17px;color:var(--text)}

/* nft */
.nft{top:3315px;height:479px}
.nft-title{left:131px;top:61px;font-size:22px}
.feature-checks{font-size:16px;line-height:22px;color:var(--text)}
.feature-checks svg{top:1px}
.nft-list{left:131px;top:145px}
.nft-list li{margin-bottom:26px}

/* soulbound */
.soulbound{top:3794px;height:447px;background:var(--band)}
.sb-art{left:133px;top:63px;width:494px;height:317px;border-radius:180px 180px 0 0}
.sb-base{left:133px;top:380px;width:494px;height:2px;background:#8a8a8a}
.sb-title{left:680px;top:57px;font-size:22px}
.sb-list{left:680px;top:140px}
.sb-list li{margin-bottom:26px}

/* clients */
.clients{top:4241px;height:296px}
.clients-title{left:0;width:1200px;top:56px;text-align:center;font-size:22px}
.client-row{position:absolute;left:110px;top:168px;width:1000px;display:flex;justify-content:space-between;align-items:center}
.client{display:flex;align-items:center;gap:8px;font-family:"Montserrat",sans-serif;font-weight:700;font-size:22px;color:#2a2a2a}
.client i{display:block;width:12px;height:12px;background:#2a2a2a;border-radius:50%}

/* footer */
.site-footer{top:4537px;height:353px;background:var(--navy);color:var(--white)}
.footer-brand{left:142px;top:122px;font-family:"Montserrat",sans-serif;font-weight:700;font-size:25px;color:var(--blue-soft)}
.footer-head{position:absolute;top:48px;font-family:"Montserrat",sans-serif;font-weight:700;font-size:13px;letter-spacing:.3px}
.footer-item{position:absolute;font-size:11.5px;line-height:15px;color:#e6ecf5}
.footer-icon{position:absolute;width:22px;height:22px;border-radius:50%;background:var(--white)}
.footer-icon svg{width:22px;height:22px;display:block}
.menu{position:absolute;left:771px;top:84px;list-style:none;font-size:11.5px;line-height:24px;color:#e6ecf5}
.copyright{left:0;width:1200px;top:300px;text-align:center;font-size:11px;color:#dfe6f0}
</style>
</head>
<body>
<svg width="0" height="0" style="position:absolute" aria-hidden="true">
  <defs>
    <symbol id="tick" viewBox="0 0 20 20">
      <path d="M16.5 7.5 A7.5 7.5 0 1 1 12.5 3" fill="none" stroke="var(--blue)" stroke-width="1.6" stroke-linecap="round"/>
      <path d="M6.5 10 l3 3 l8-8.5" fill="none" stroke="var(--blue)" stroke-width="1.8" stroke-linecap="round" stroke-linejoin="round"/>
    </symbol>
    <symbol id="tick-dark" viewBox="0 0 20 20">
      <circle cx="10" cy="10" r="7.5" fill="none" stroke="#333" stroke-width="1.4"/>
      <path d="M6.5 10 l2.5 2.5 l5-5" fill="none" stroke="#333" stroke-width="1.6" stroke-linecap="round" stroke-linejoin="round"/>
    </symbol>
  </defs>
</svg>

<div class="page">

  <header class="section site-header">
    <div class="brand"><span class="brand-mark"></span>NineHalfMark</div>
    <nav class="nav">
      <span class="active">HOME</span><span>ABOUT US</span><span>SERVICES</span><span>SOLUTIONS</span><span>BLOG</span><span>CONTACT US</span>
    </nav>
  </header>

  <section class="section hero">
    <div class="abs hero-kicker">Indonesia’s Web 3.0 Project</div>
    <h1 class="abs hero-title">OBSTACLES</h1>
    <ul class="check-list hero-list">
      <li><svg><use href="#tick"/></svg>High effort to educate user about web3 technology<br>especially in web3 wallets</li>
      <li><svg><use href="#tick"/></svg>Limited support to develop web 3.0 based projects<br>such as Sandbox and NFT Launcher</li>
      <li><svg><use href="#tick"/></svg>Limited availability of web 3.0 developer</li>
      <li><svg><use href="#tick"/></svg>High latency due to lack of Indonesia based<br>RPC nodes.</li>
    </ul>
    <div class="btn" style="left:131px;top:397px;width:118px;height:34px">READ MORE</div>
    <div class="visual hero-photo" role="img" aria-label="Photo of a smiling developer in glasses working on a laptop in a bright office"></div>
  </section>

  <section class="section nutshell">
    <div class="diagram-label" style="left:363px;top:61px">DECENTRALIZATION</div>
    <div class="diagram-label" style="left:215px;top:145px">ENCRYPTION</div>
    <div class="diagram-label" style="left:507px;top:145px">IMMUTABILITY</div>
    <div class="diagram-label" style="left:272px;top:377px">DISTRIBUTION</div>
    <div class="diagram-label" style="left:443px;top:377px">TOKENIZATION</div>
    <div class="visual diagram-art" role="img" aria-label="Diagram of five hexagon nodes joined in a ring by chain links, one for each blockchain property"></div>
    <h2 class="abs heading nutshell-title">BLOCKCHAIN IN A NUTSHELL</h2>
    <div class="rule" style="left:638px;top:111px;width:152px"></div>
    <p class="abs nutshell-copy">Blockchain is a distributed, encrypted, immutable ledger that can also incorporates technologies such as asset tokenization and smart contracts. With its decentralized and immutable property, blockchain is a revolutionary technology that addresses problems with fraudulent activities.</p>
    <div class="btn" style="left:640px;top:350px;width:127px;height:34px">READ MORE</div>
  </section>

  <section class="section trust">
    <div class="abs trust-kicker">Blockchain as a</div>
    <h2 class="abs heading trust-title">TRUST SYSTEM</h2>
    <div class="abs trust-sub">Imagine a database that is...</div>
    <div class="rule" style="left:571px;top:150px"></div>

    <div class="trust-card" style="left:133px">
      <svg viewBox="0 0 52 52" fill="none" stroke="var(--blue)" stroke-width="2"><rect x="6" y="6" width="16" height="12" rx="2"/><rect x="30" y="32" width="16" height="12" rx="2"/><path d="M14 18 v14 h16" stroke-dasharray="3 3"/><path d="M38 32 v-14 h-16" stroke-dasharray="3 3"/></svg>
      <p>Replicated all<br>around the<br>world</p>
    </div>
    <div class="trust-card" style="left:323px">
      <svg viewBox="0 0 52 52" fill="none" stroke="var(--blue)" stroke-width="2"><rect x="6" y="22" width="40" height="22" rx="2"/><path d="M16 22 v-8 a10 10 0 0 1 20 0 v8"/><path d="M14 33 h4 M24 33 h4 M34 33 h4"/></svg>
      <p>Encrypted,<br>secure and<br>immutable</p>
    </div>
    <div class="trust-card" style="left:513px">
      <svg viewBox="0 0 52 52" fill="none" stroke="var(--blue)" stroke-width="2"><rect x="4" y="8" width="44" height="30" rx="2"/><path d="M18 46 h16 M26 38 v8"/><rect x="10" y="15" width="9" height="8"/><rect x="22" y="15" width="9" height="8"/><rect x="34" y="15" width="8" height="8"/></svg>
      <p>Can only use<br>Insert method</p>
    </div>
    <div class="trust-card" style="left:705px">
      <svg viewBox="0 0 52 52" fill="none" stroke="var(--blue)" stroke-width="2"><rect x="4" y="8" width="44" height="32" rx="2"/><circle cx="26" cy="22" r="8"/><path d="M20 40 a6 6 0 0 1 12 0"/><path d="M26 14 v-4 M26 34 v-4"/></svg>
      <p>Every insertion<br>tied to specific<br>identity</p>
    </div>
    <div class="trust-card" style="left:893px">
      <svg viewBox="0 0 52 52" fill="none" stroke="var(--blue)" stroke-width="2"><rect x="4" y="10" width="44" height="28" rx="2"/><rect x="12" y="18" width="8" height="7"/><rect x="22" y="18" width="8" height="7"/><rect x="32" y="18" width="8" height="7"/><path d="M12 31 h28 M18 44 h16"/></svg>
      <p>Every insertion<br>are validated<br>by multiple<br>parties</p>
    </div>
  </section>

  <section class="section products">
    <article class="product-card" style="left:131px;top:0">
      <div class="product-brand">NINEHALFMARK</div>
      <h3 class="product-title">WHITELABEL WEB3 WALLET</h3>
      <p class="product-sub">let you focus on your businesses</p>
      <div class="product-art" role="img" aria-label="Illustration of a woman presenting a phone wallet app with coins" style="background:linear-gradient(135deg,#e9ecf8,#c9d3f1 60%,#f1c46a)"></div>
      <ul class="feature-list">
        <li style="left:36px;top:381px">Familiar User Interface</li>
        <li style="left:228px;top:381px">Passwords and OTP codes</li>
        <li style="left:36px;top:416px">Safe Non-Custodial Type</li>
        <li style="left:228px;top:416px">Perform perfectly the same<br>as other Web3 Wallet</li>
      </ul>
    </article>
    <article class="product-card" style="left:614px;top:0">
      <div class="product-brand">NINEHALFMARK</div>
      <h3 class="product-title">RPC NODES</h3>
      <p class="product-sub">makes your transaction faster and more reliable</p>
      <div class="product-art" role="img" aria-label="Illustration of a person beside a globe with a target and gears" style="background:linear-gradient(135deg,#d9e6d2,#8a9be8 55%,#5b6fd8)"></div>
      <ul class="feature-list">
        <li style="left:18px;top:380px;width:245px">First Indonesian RPC Nodes, most<br>RPC Nodes are US/EU based.</li>
        <li style="left:18px;top:430px;width:245px">15x faster than default RPC Nodes</li>
        <li style="left:276px;top:360px;width:160px">Automatically included in any of NineHalfMark product</li>
        <li style="left:276px;top:420px;width:160px">In partnership with one of the biggest server provider in Indonesia</li>
      </ul>
    </article>
    <article class="product-card" style="left:131px;top:513px">
      <div class="product-brand">NINEHALFMARK</div>
      <h3 class="product-title">BLOCKCHAIN API</h3>
      <p class="product-sub">makes your token development easier,<br>develop web3 project with web2 knowledge.</p>
      <div class="product-art" role="img" aria-label="Illustration of a developer with a laptop beside a screen of blocks, server stacks and gold coins" style="top:155px;height:205px;background:linear-gradient(135deg,#7c8fe6,#f2c46b 55%,#5fa58e)"></div>
      <ul class="feature-list">
        <li style="left:36px;top:389px">Token API</li>
        <li style="left:228px;top:389px">Web3 Auth</li>
        <li style="left:36px;top:424px">NFT API</li>
        <li style="left:228px;top:424px">Notification API</li>
      </ul>
    </article>
    <article class="product-card" style="left:614px;top:513px">
      <div class="product-brand" style="top:28px">NINEHALFMARK</div>
      <h3 class="product-title" style="top:55px">WEB3 SANDBOX</h3>
      <p class="product-sub" style="top:85px">makes your smart contract development smoother</p>
      <div class="product-art" role="img" aria-label="Illustration of two people stacking colorful cubes on a purple backdrop" style="top:130px;height:210px;background:linear-gradient(135deg,#a58af0,#7a5ae0 55%,#f0a0c8)"></div>
      <ul class="feature-list">
        <li style="left:36px;top:382px;width:360px">Best from the only other 2 Sandbox in the World.</li>
        <li style="left:36px;top:410px;width:360px">Get sandbox native token easier</li>
        <li style="left:36px;top:437px;width:360px">Make Web3 development 80% faster</li>
      </ul>
    </article>
  </section>

  <section class="section team">
    <h2 class="abs heading team-title">MEET OUR TEAMS</h2>
    <div class="abs team-sub">we will help you to tap in web3 ecosystems</div>
    <div class="rule" style="left:571px;top:124px"></div>

    <article class="member" style="left:131px">
      <div class="member-photo" role="img" aria-label="Portrait of the CEO in glasses and a light jacket" style="background:linear-gradient(160deg,#6f8a55,#a9b99a 60%,#d4dccb)"></div>
      <div class="member-name">RENDRA KUSUMA</div>
      <div class="member-role">CEO</div>
      <p class="member-bio">Building infrastructure for digital<br>billing in Indonesia since 2005</p>
    </article>
    <article class="member" style="left:452px">
      <div class="member-photo" role="img" aria-label="Portrait of the CTO in glasses and a white shirt" style="background:linear-gradient(160deg,#f1f1f1,#e2e2e2 60%,#d6d6d6)"></div>
      <div class="member-name">BAYU PRATAMA</div>
      <div class="member-role">CTO</div>
      <p class="member-bio">Ledger 30 under 30 Asia<br>Indonesia Tech Rockstar</p>
    </article>
    <article class="member" style="left:773px">
      <div class="member-photo" role="img" aria-label="Portrait of the founding team member in a dark suit" style="background:linear-gradient(160deg,#e9ecef,#bfc6cc 55%,#2b2f36)"></div>
      <div class="member-name">DARREN HALIM</div>
      <div class="member-role">Founding Team</div>
      <p class="member-bio">Web3 Serial Entrepreneur with history<br>in founding Web3 Game and Launchpad</p>
    </article>
  </section>

  <section class="section nft">
    <h2 class="abs heading nft-title">NFT STARTER</h2>
    <ul class="check-list feature-checks nft-list">
      <li><svg><use href="#tick-dark"/></svg>NFT Minting, Transfer and Burn</li>
      <li><svg><use href="#tick-dark"/></svg>As easy as image upload</li>
      <li><svg><use href="#tick-dark"/></svg>Customizable rule and use case</li>
      <li><svg><use href="#tick-dark"/></svg>Supporting Soul-Bound Token</li>
    </ul>
    <div class="btn" style="left:131px;top:360px;width:127px;height:34px">READ MORE</div>
    <div class="visual" role="img" aria-label="Illustration of a secure web platform surrounded by cloud, lock, shield, servers, safe and coin icons" style="left:604px;top:52px;width:388px;height:348px;border-radius:24px;background:linear-gradient(135deg,#dfe9fb,#9ec0f4 55%,#f5d36a)"></div>
  </section>

  <section class="section soulbound">
    <div class="visual sb-art" role="img" aria-label="Illustration of a jumping man celebrating above stacks of gold coins and a rising arrow" style="background:linear-gradient(160deg,#e7edf9,#cfdaf2 55%,#f3c85c)"></div>
    <div class="abs sb-base"></div>
    <h2 class="abs heading sb-title">SOULBOUND TOKEN STARTER</h2>
    <ul class="check-list feature-checks sb-list">
      <li><svg><use href="#tick-dark"/></svg>Lorem Ipsum is simply dummy text of the</li>
      <li><svg><use href="#tick-dark"/></svg>There are many variations of passages of L</li>
      <li><svg><use href="#tick-dark"/></svg>Contrary to popular belief, Lorem</li>
      <li><svg><use href="#tick-dark"/></svg>The standard chunk of Lorem</li>
    </ul>
    <div class="btn" style="left:680px;top:354px;width:126px;height:33px">READ MORE</div>
  </section>

  <section class="section clients">
    <h2 class="abs heading clients-title">OUR CLIENTS</h2>
    <div class="rule" style="left:521px;top:95px;width:158px"></div>
    <div class="client-row">
      <span class="client">Meridian</span>
      <span class="client">Strider</span>
      <span class="client">Tristar</span>
      <span class="client"><i></i>Autoveld</span>
      <span class="client">Kestrel</span>
      <span class="client"><i></i>Greenbean</span>
    </div>
  </section>

  <footer class="section site-footer">
    <div class="abs footer-brand">NineHalfMark</div>

    <div class="footer-head" style="left:391px">CONTACT US</div>
    <div class="footer-icon" style="left:391px;top:86px"><svg viewBox="0 0 22 22"><path d="M11 5 a4 4 0 0 1 4 4 c0 3-4 8-4 8 s-4-5-4-8 a4 4 0 0 1 4-4z" fill="var(--navy)"/><circle cx="11" cy="9" r="1.5" fill="#fff"/></svg></div>
    <div class="footer-item" style="left:424px;top:84px">Suite 204, Level 2 West,<br>410-418 Harbour Road, Eastvale VIC 3390.</div>
    <div class="footer-icon" style="left:391px;top:136px"><svg viewBox="0 0 22 22"><path d="M7.5 6 l2.5 0 l1 3 l-1.5 1 a7 7 0 0 0 2.5 2.5 l1-1.5 l3 1 l0 2.5 a1.5 1.5 0 0 1-1.5 1.5 a9 9 0 0 1-8.5-8.5 a1.5 1.5 0 0 1 1.5-1.5z" fill="var(--navy)"/></svg></div>
    <div class="footer-item" style="left:424px;top:134px">Call Us<br>+1 555 014 2290</div>
    <div class="footer-icon" style="left:391px;top:186px"><svg viewBox="0 0 22 22"><rect x="5" y="7" width="12" height="9" rx="1" fill="var(--navy)"/><path d="M5.5 7.5 l5.5 4.5 l5.5-4.5" fill="none" stroke="#fff" stroke-width="1.2"/></svg></div>
    <div class="footer-item" style="left:424px;top:184px">E mail Us<br>hello@NineHalfMark.com</div>

    <div class="footer-head" style="left:771px">MENU</div>
    <ul class="menu">
      <li>HOME</li><li>ABOUT US</li><li>SERVICES</li><li>SOLUTIONS</li><li>BLOG</li><li>CONTACT US</li>
    </ul>

    <div class="footer-head" style="left:971px">FOLLOW US</div>
    <div class="footer-icon" style="left:971px;top:86px"></div>
    <div class="footer-item" style="left:1003px;top:84px">Like us on<br>PALBOOK</div>
    <div class="footer-icon" style="left:971px;top:136px"></div>
    <div class="footer-item" style="left:1003px;top:134px">Follow us on<br>CHIRPER</div>
    <div class="footer-icon" style="left:971px;top:186px"></div>
    <div class="footer-item" style="left:1003px;top:184px">Follow us on<br>LINKFOLD</div>

    <div class="abs copyright">Copyright © 2023 All Rights Reserved</div>
  </footer>

</div>
</body>
</html>
```